Bright K's Auto Detailing new business cards

I am a business owner who professionally details cars. I clean and detail the interiors, exteriors of vehicles. I need a logo designed for my new business Bright K's Auto Detailing and a great designed card that will wow anyone that I hand it out to. Attached is a photo that I would like on side of the card. I want the picture to be on the right side of the card, while my busines name will be on the other side. I want the picture to have a slant where it divided the card into left and right, not just straight down. The picture will be printed glossy and I want the left half to have a carbon fiber background. Feel free to design a cool font for the business name, The business name needs to be a red gloss to pop out against the matte background. The back of the card should have my name Colin Marchetti. Under my name should be Owner/ Operator. then all my contact info and fb and instagram stuff. must include services offered- Paint Correction, Exterior detailing
Interior Detailing, Engine Bay Detailing, Headlight restoration, Ceramic Coatings

Target Market(s)

My target market is anyone who drives a vehicle.

Industry/Entity Type

Automotive

Contact Information for Business Card

Business name- Bright K's Auto Detailing
Colin Marchetti Owner/ Operator
Location- Alder Springs, CA
Business # (559) 214-6079
email- colin@thebrightpolisher.example
fb and instragram logos- @thebrightpolisher

Font styles to use
Serif
Script
Other font styles liked:
• Blacksword

Colors
ec1f27
000000

Requirements
Must have
• The card must be in landscape position. All the details that are in the brief description which are my business name, my name, services offered and any other info thats in the project description. I uploaded pics of veltranos that I would like to see different designs incorporated into the backside of the card. File 5,6,and 7 are ideas that I would like to see done with my business name. The diamond around my name with the polisher coming around the bottom, and a Veltrano outline on the left side of the diamond kinda like file 5
• Also, business name and name should be in some style of script, while the rest of the fonts in serif. Must have the picture of me on the front right side of the card!!!
Nice to have
• Your own personal ideas that you think I am missing.
Should not have
• No grafitti, no generic logos around the business name like every other auto detail card on google.

```html
<!DOCTYPE html>
<html lang="en">
<head>
<meta charset="utf-8">
<title>Bright K's Auto Detailing — Business Cards</title>
<link rel="stylesheet" href="https://fonts.googleapis.com/css2?family=Kaushan+Script&family=Lato:wght@400;700&display=swap">
<style>
  :root {
    --brand-red: #ec1f27;
    --card-black: #050505;
    --ink-white: #f2f2f2;
    --backdrop: #e9e6e1;
  }
  * { box-sizing: border-box; margin: 0; padding: 0; }
  html, body { width: 1200px; height: 900px; overflow: hidden; }
  body {
    background: var(--backdrop);
    font-family: "Lato", "Helvetica Neue", Arial, sans-serif;
    position: relative;
  }
  .card {
    position: absolute;
    width: 620px;
    height: 354px;
    background: var(--card-black);
    border-radius: 6px;
    overflow: hidden;
    box-shadow: 0 14px 30px rgba(0,0,0,0.28);
    color: var(--ink-white);
  }
  .card--front { left: 80px; top: 70px; }
  .card--back  { left: 500px; top: 470px; }

  .photo { position: absolute; top: 0; right: 0; bottom: 0; }
  .card--front .photo {
    width: 290px;
    clip-path: polygon(28% 0, 100% 0, 100% 100%, 0 100%);
    background: radial-gradient(circle at 42% 68%, #d9e4f4 0%, #5c7290 14%, #1d2a40 38%, #0b0f18 75%);
  }
  .card--back .photo {
    width: 330px;
    clip-path: polygon(22% 0, 100% 0, 100% 100%, 0 100%);
    background: linear-gradient(160deg, #2b2b2d 0%, #131314 45%, #060606 100%);
  }

  .wordmark {
    position: absolute;
    font-family: "Lato", "Helvetica Neue", Arial, sans-serif;
    font-weight: 700;
    color: var(--brand-red);
    line-height: 1.15;
    letter-spacing: 0.5px;
  }
  .card--front .wordmark { left: 60px; top: 112px; font-size: 30px; }
  .card--back .wordmark  { left: 48px; top: 42px;  font-size: 30px; }

  .services {
    position: absolute;
    left: 0; right: 0; bottom: 48px;
    text-align: center;
    font-size: 15px;
    line-height: 1.5;
  }
  .services .divider { color: var(--brand-red); margin: 0 5px; }

  .owner { position: absolute; left: 60px; top: 170px; }
  .owner__name {
    font-family: "Kaushan Script", "Brush Script MT", cursive;
    color: var(--brand-red);
    font-size: 30px;
  }
  .owner__title { font-size: 17px; margin-top: 2px; }

  .contact { position: absolute; left: 76px; top: 250px; list-style: none; }
  .contact li { display: flex; align-items: center; gap: 8px; font-size: 16px; line-height: 1.55; }
  .contact svg { width: 14px; height: 14px; fill: var(--brand-red); flex: none; }

  .social {
    position: absolute; right: 22px; top: 190px;
    display: flex; align-items: center; gap: 8px;
    font-size: 14px;
  }
  .social__mark { width: 12px; height: 12px; border-radius: 50%; background: var(--ink-white); }
</style>
</head>
<body>

  <section class="card card--front" aria-label="Card front">
    <div class="photo" role="img" aria-label="Photo of the owner polishing a car with an orange-gloved hand and a rotary polisher under a bright work light"></div>
    <h1 class="wordmark">Bright K's<br>Auto Detailing</h1>
    <p class="services">
      Paint Correction<span class="divider">|</span>Exterior detailing<span class="divider">|</span>Interior Detailing<br>
      Engine Bay Detailing<span class="divider">|</span>Headlight restoration<span class="divider">|</span>Ceramic Coatings
    </p>
  </section>

  <section class="card card--back" aria-label="Card back">
    <div class="photo" role="img" aria-label="Dark studio photo of a black sports car in side profile"></div>
    <h2 class="wordmark">Bright K's<br>Auto Detailing</h2>
    <div class="owner">
      <p class="owner__name">Colin Marchetti</p>
      <p class="owner__title">Owner/ Operator</p>
    </div>
    <ul class="contact">
      <li>
        <svg viewBox="0 0 24 24" aria-hidden="true"><path d="M6.6 10.8a15.1 15.1 0 0 0 6.6 6.6l2.2-2.2c.3-.3.7-.4 1-.2 1.1.4 2.3.6 3.6.6.6 0 1 .4 1 1V20c0 .6-.4 1-1 1A17 17 0 0 1 3 4c0-.6.4-1 1-1h3.5c.6 0 1 .4 1 1 0 1.3.2 2.5.6 3.6.1.3 0 .7-.2 1z"/></svg>
        (559) 214-6079
      </li>
      <li>
        <svg viewBox="0 0 24 24" aria-hidden="true"><path d="M2 5h20v14H2z M2 5l10 8 10-8" stroke="#050505" stroke-width="1.5"/></svg>
        colin@thebrightpolisher.example
      </li>
      <li>
        <svg viewBox="0 0 24 24" aria-hidden="true"><path d="M12 2a7 7 0 0 0-7 7c0 5.2 7 13 7 13s7-7.8 7-13a7 7 0 0 0-7-7zm0 9.5A2.5 2.5 0 1 1 12 6.5a2.5 2.5 0 0 1 0 5z"/></svg>
        Alder Springs, CA
      </li>
    </ul>
    <div class="social">
      <span class="social__mark" aria-hidden="true"></span>
      <p>@thebrightpolisher</p>
    </div>
  </section>

</body>
</html>
```